Clinical Layout Builders - Stationery
Biz Cards + Stationary
Clinical Layout Builders - Stationery - Information Technology
Creative Brief
Professional
Dr. Elena M. Castillo
Director of Content Development
Ceiba Business Plaza #3, Suite 118 San Juan, PR 00941
(787) PENDING
elena.castillo@hnvwqbt.com
www.hnvwqbt.com
Need a second set of cards for: Dr. Luis F. Beltran Business Development Director Same info- address, fax and phone (Pending) Cell: (787) 555-0192 Email: luis.beltran@hnvwqbt.com
Either the logo, the website or something else. Feel free to be creative!

```html
<!DOCTYPE html>
<html lang="en">
<head>
<meta charset="utf-8">
<title>Clinical Layout Builders – Business Card</title>
<link href="https://fonts.googleapis.com/css2?family=Open+Sans:wght@400;600;700&display=swap" rel="stylesheet">
<style>
  :root {
    --page-bg: #ececea;
    --card-bg: #ffffff;
    --magenta: #9c1f73;
    --magenta-light: #c43d96;
    --grey: #6d6e70;
    --grey-light: #a7a8aa;
    --name-blue: #1f5fbf;
    --text: #3c3c3c;
  }
  * { margin: 0; padding: 0; box-sizing: border-box; }
  html, body {
    width: 1200px; height: 935px; overflow: hidden;
    background: var(--page-bg);
    font-family: "Open Sans", Arial, sans-serif;
  }
  .card {
    position: absolute;
    left: 80px; top: 197px;
    width: 1040px; height: 541px;
    background: var(--card-bg);
    border-radius: 48px;
    overflow: hidden;
    box-shadow: 0 6px 18px rgba(0,0,0,0.18);
  }
  .card-swoosh { position: absolute; inset: 0; width: 100%; height: 100%; }
  .brand {
    position: absolute;
    left: 228px; top: 40px;
    display: flex; align-items: center; gap: 18px;
    white-space: nowrap;
  }
  .brand-mark {
    width: 38px; height: 38px;
    background: var(--magenta);
  }
  .brand-name {
    font-weight: 700;
    font-size: 40px;
    letter-spacing: 0.5px;
    color: var(--magenta);
    text-transform: uppercase;
  }
  .person {
    position: absolute;
    right: 535px; top: 372px;
    text-align: right;
    white-space: nowrap;
  }
  .person-name {
    font-weight: 700;
    font-size: 30px;
    color: var(--name-blue);
    line-height: 1.2;
  }
  .person-title {
    font-size: 20px;
    color: var(--text);
    margin-top: 2px;
  }
  .contact {
    position: absolute;
    left: 530px; top: 296px;
    font-size: 19px;
    line-height: 30px;
    color: var(--text);
    list-style: none;
    white-space: nowrap;
  }
  .contact-label {
    font-weight: 700;
    color: var(--magenta);
    display: inline-block;
    width: 32px;
  }
</style>
</head>
<body>
  <section class="card" aria-label="Business card">
    <svg class="card-swoosh" viewBox="0 0 1040 541" preserveAspectRatio="none" aria-hidden="true">
      <defs>
        <linearGradient id="bandMagenta" x1="0" y1="0" x2="1" y2="1">
          <stop offset="0" stop-color="#c43d96"/>
          <stop offset="1" stop-color="#8a1763"/>
        </linearGradient>
      </defs>
      <path d="M0 150 C40 300 140 420 330 541 L0 541 Z" fill="#a7a8aa"/>
      <path d="M0 175 C30 310 110 420 280 541 L0 541 Z" fill="url(#bandMagenta)"/>
      <path d="M900 0 C990 120 970 360 870 541 L1040 541 L1040 0 Z" fill="#6d6e70"/>
      <path d="M930 0 C1015 120 1005 360 910 541 L1040 541 L1040 0 Z" fill="url(#bandMagenta)"/>
    </svg>

    <div class="brand">
      <span class="brand-mark"></span>
      <span class="brand-name">Clinical Layout Builders</span>
    </div>

    <div class="person">
      <p class="person-name">Dr. Elena M. Castillo</p>
      <p class="person-title">Director of Content Development</p>
    </div>

    <ul class="contact">
      <li>Ceiba Business Plaza #3, Suite 118</li>
      <li>San Juan, PR 00941</li>
      <li><span class="contact-label">P :</span>(787) PENDING</li>
      <li><span class="contact-label">C :</span>(787) 555-0148</li>
      <li><span class="contact-label">F :</span>(787) 555-0173</li>
      <li><span class="contact-label">E :</span>elena.castillo@hnvwqbt.com</li>
      <li><span class="contact-label">W :</span>www.hnvwqbt.com</li>
    </ul>
  </section>
</body>
</html>
```